Business Card and Stationary
Cutting Edge Medical Office
Modern
Dr. Paul Drembley
Chiropractor
418 Calder St S
Lake Norvale, ND 58001
NorvaleSpine@example.com
NorvaleSpine.example
I have a cutting edge chiropractic office where we basically do everything different. We use a lot of Bright Path Systems and have a lot of fun in the office. I need my business card and stationary to reflect that.
For Vector File of logo, please download this link:
http://www.filedrop.example/downloads/x9k2m4p7q1r8s3t6v0w5y2z4a7b1c9d3/482263
I for sure do want rounded corners and a double sided business card. I am going to print it on silk so it will look really cool. I would like to make a branding impression and have a swoop with my globe in the upper left on all my stationary designs. On the card it would be great to have a map of where my office is on the back of the card as well as a QR Code as well.
For the actual envelope, there are some restrictions with the design. On the front, there cand really be anything on the bottom half of the envelope. That is because the need that space empty for scanners and whatnot.
Vita Ridge Logo 2D
JPEG file of the Windows
My 3D VR Logo
My 3D VR Logo with Stroke
I am going to be putting a View-Through on all of these windows and doors. I am looking for the same kind of branding to be consistent with my business card as well.

```html
<!DOCTYPE html>
<html lang="en">
<head>
<meta charset="utf-8">
<title>Vita Ridge – Business Card</title>
<link rel="stylesheet" href="https://fonts.googleapis.com/css2?family=Titillium+Web:wght@400;600;700;900&display=swap">
<style>
  :root {
    --page-bg: #e9eaec;
    --card-bg: #ffffff;
    --brand-blue: #1f9ad6;
    --brand-blue-deep: #0f78b8;
    --brand-green: #7cc242;
    --brand-green-deep: #5aa62c;
    --text-dark: #3a3f44;
    --text-muted: #6a7077;
    --shadow: rgba(30, 40, 50, 0.18);
  }
  * { box-sizing: border-box; margin: 0; padding: 0; }
  html, body {
    width: 1200px; height: 864px; overflow: hidden;
    background: var(--page-bg);
    font-family: "Titillium Web", sans-serif;
  }
  .stage {
    position: relative; width: 1200px; height: 864px;
    display: flex; align-items: center; justify-content: center; gap: 60px;
  }
  .card {
    position: relative; width: 530px; height: 310px;
    background: var(--card-bg);
    border-radius: 22px;
    overflow: hidden;
    box-shadow: 0 10px 28px var(--shadow);
  }
  .brand-name {
    display: flex; align-items: center; gap: 10px;
    font-weight: 900; color: var(--brand-blue);
    letter-spacing: 0.5px; line-height: 1;
  }
  .brand-dot {
    display: inline-block; border-radius: 50%;
    background: var(--brand-green);
  }
  /* front */
  .card-front { display: flex; flex-direction: column; align-items: center; justify-content: center; }
  .card-front .brand-name { font-size: 64px; }
  .card-front .brand-dot { width: 34px; height: 34px; }
  .front-web {
    margin-top: 34px; font-size: 15px; letter-spacing: 3px;
    color: var(--text-dark);
  }
  /* back */
  .back-swoosh { position: absolute; inset: 0; width: 100%; height: 100%; }
  .card-back .brand-name {
    position: absolute; left: 32px; top: 52px; font-size: 44px;
  }
  .card-back .brand-dot { width: 26px; height: 26px; }
  .doctor {
    position: absolute; left: 78px; top: 150px;
  }
  .doctor-name { font-size: 16px; font-weight: 600; color: var(--brand-blue-deep); line-height: 1.2; }
  .doctor-title { font-size: 14px; color: var(--text-dark); }
  .contact-list {
    position: absolute; left: 326px; top: 42px; list-style: none;
    font-size: 13px; color: var(--text-dark); line-height: 1.25;
  }
  .contact-list li { display: flex; align-items: flex-start; gap: 8px; margin-bottom: 3px; }
  .contact-icon {
    flex: none; width: 16px; height: 16px; border-radius: 50%;
    background: var(--text-muted); margin-top: 1px;
    display: flex; align-items: center; justify-content: center;
  }
  .contact-icon svg { width: 10px; height: 10px; fill: #fff; }
</style>
</head>
<body>
<main class="stage">

  <section class="card card-front" aria-label="Business card front">
    <div class="brand-name"><span class="brand-dot"></span>VitaRidge</div>
    <p class="front-web">www.NorvaleSpine.example</p>
  </section>

  <section class="card card-back" aria-label="Business card back">
    <svg class="back-swoosh" viewBox="0 0 530 310" preserveAspectRatio="none" aria-hidden="true">
      <defs>
        <linearGradient id="blueBand" x1="0" y1="0" x2="1" y2="1">
          <stop offset="0" stop-color="#3bb3e8"/>
          <stop offset="1" stop-color="#0f78b8"/>
        </linearGradient>
        <linearGradient id="greenBand" x1="0" y1="0" x2="1" y2="0">
          <stop offset="0" stop-color="#5aa62c"/>
          <stop offset="1" stop-color="#8fd04f"/>
        </linearGradient>
      </defs>
      <path d="M0 200 C 110 200 210 240 290 310 L 0 310 Z" fill="url(#blueBand)"/>
      <path d="M0 258 C 150 218 300 228 430 310 L 0 310 Z" fill="#ffffff"/>
      <path d="M0 266 C 150 228 300 238 420 310 L 0 310 Z" fill="url(#greenBand)"/>
      <path d="M0 286 C 130 262 250 272 330 310 L 0 310 Z" fill="#ffffff"/>
      <path d="M0 292 C 120 272 240 282 310 310 L 0 310 Z" fill="url(#blueBand)"/>
    </svg>

    <div class="brand-name"><span class="brand-dot"></span>VitaRidge</div>

    <div class="doctor">
      <p class="doctor-name">Dr. Paul Drembley</p>
      <p class="doctor-title">Chiropractor</p>
    </div>

    <ul class="contact-list">
      <li>
        <span class="contact-icon"><svg viewBox="0 0 10 10"><path d="M5 0a3.5 3.5 0 0 0-3.5 3.5C1.5 6 5 10 5 10s3.5-4 3.5-6.5A3.5 3.5 0 0 0 5 0zm0 5a1.5 1.5 0 1 1 0-3 1.5 1.5 0 0 1 0 3z"/></svg></span>
        <span>418 Calder St S<br>Lake Norvale, ND 58001</span>
      </li>
      <li>
        <span class="contact-icon"><svg viewBox="0 0 10 10"><path d="M2 0l2 2-1 1.5a6 6 0 0 0 3.5 3.5L8 6l2 2-1.5 2C4 10 0 6 0 1.5z"/></svg></span>
        <span>555-014-2550</span>
      </li>
      <li>
        <span class="contact-icon"><svg viewBox="0 0 10 10"><path d="M2 0l2 2-1 1.5a6 6 0 0 0 3.5 3.5L8 6l2 2-1.5 2C4 10 0 6 0 1.5z"/></svg></span>
        <span>555-018-7055</span>
      </li>
      <li>
        <span class="contact-icon"><svg viewBox="0 0 10 10"><path d="M0 2h10v6H0zM0 2l5 3.5L10 2" stroke="#fff" stroke-width="0.8" fill="none"/></svg></span>
        <span>NorvaleSpine@example.com</span>
      </li>
      <li>
        <span class="contact-icon"><svg viewBox="0 0 10 10"><circle cx="5" cy="5" r="4.3" stroke="#fff" stroke-width="0.9" fill="none"/><path d="M0.7 5h8.6M5 0.7c-2 2.4-2 6.2 0 8.6M5 0.7c2 2.4 2 6.2 0 8.6" stroke="#fff" stroke-width="0.8" fill="none"/></svg></span>
        <span>www.NorvaleSpine.example</span>
      </li>
    </ul>
  </section>

</main>
</body>
</html>
```